Signage for events and farmers market for Chocolate company.

I need a great sign that will hang at events such as bridal expose, farmers markets, conventions, food truck stand. Something that can will catch customers attention but also show what my company's about.

Copper Lantern Sweets is a local handmade chocolate company here in Austin Texas. Our chocolate is vegan gluten free organic faire trade handmade chocolate that is locally made. I want to have all this as points on the signage. We sell boxes, piece by piece and can take custom orders for events. Weddings birthday parties. You want it I'll do my best to make it kind of company. I want the signage to reflect well with our brand identity. I'd love to see what you come up with. The sign will need to be large to expo tables and to fit on a pop up tent for the farmers market. If you have any questions please feel free to ask.

I'd also like our website on the banner
Copperlanternsweetsatx.com
512.637.4185
Locally made in Austin Tx
Hand made
Check us out on Instagram: copperlanternsweets

```html
<!DOCTYPE html>
<html lang="en">
<head>
<meta charset="utf-8">
<title>Copper Lantern Sweets – Event Banner</title>
<link rel="stylesheet" href="https://fonts.googleapis.com/css2?family=Questrial&family=Roboto+Condensed:wght@400;700&display=swap">
<style>
  :root {
    --ink: #1a1a1a;
    --red: #e2131f;
    --teal: #00606b;
    --mist: #d3e4e6;
    --mist-light: #e3eeef;
    --frame: #2f6f78;
    --paper: #ffffff;
  }
  html, body {
    margin: 0;
    padding: 0;
    width: 1200px;
    height: 1000px;
    overflow: hidden;
    background: var(--paper);
  }
  .canvas {
    position: relative;
    width: 1200px;
    height: 1000px;
  }
  .cover-note {
    position: absolute;
    left: 88px;
    top: 80px;
    font-family: "Questrial", sans-serif;
    font-size: 14px;
    line-height: 17px;
    color: var(--ink);
  }
  .cover-note p { margin: 0 0 16px; }
  .banner {
    position: absolute;
    left: 45px;
    top: 305px;
  }
  .claim { font-family: "Roboto Condensed", sans-serif; fill: var(--red); font-size: 30px; }
  .phone { font-family: "Questrial", sans-serif; fill: var(--teal); font-size: 26px; letter-spacing: 2px; }
  .brand-name { font-family: "Roboto Condensed", sans-serif; fill: var(--red); font-size: 34px; font-weight: 400; }
  .web { font-family: "Roboto Condensed", sans-serif; fill: var(--red); font-size: 27px; letter-spacing: 1px; }
  .social { font-family: "Roboto Condensed", sans-serif; fill: var(--teal); font-size: 20px; letter-spacing: 1px; }
  .social-handle { font-weight: 700; }
  .star { fill: var(--teal); }
</style>
</head>
<body>
<div class="canvas">
  <div class="cover-note">
    <p>Hi Dana,</p>
    <p>This is the last banner with our modifications. I think it work better and nice.<br>
    I stay open to any modificacations / upgrade.<br>
    Please give feedback</p>
    <p>I haven’t received feed back on T-shirt proposals.</p>
  </div>

  <svg class="banner" width="1110" height="413" viewBox="0 0 1110 413" xmlns="http://www.w3.org/2000/svg">
    <defs>
      <polygon id="star" points="0,-10 2.9,-3.1 9.5,-3.1 4.2,1.4 6.2,8.5 0,4.3 -6.2,8.5 -4.2,1.4 -9.5,-3.1 -2.9,-3.1"/>
    </defs>
    <rect class="field" x="0.5" y="0.5" width="1109" height="412" fill="var(--paper)" stroke="var(--frame)"/>

    <!-- side bands -->
    <polygon points="1,1 85,1 55,206 85,412 1,412" fill="var(--mist-light)"/>
    <polygon points="1109,1 1025,1 1055,206 1025,412 1109,412" fill="var(--mist-light)"/>
    <rect role="img" aria-label="Column of small white stars" x="10" y="10" width="40" height="393" fill="var(--mist)"/>
    <rect role="img" aria-label="Column of small white stars" x="1060" y="10" width="40" height="393" fill="var(--mist)"/>

    <!-- central hourglass panel -->
    <polygon points="350,1 760,1 715,206 760,412 350,412 395,206" fill="var(--mist)"/>
    <polygon points="455,1 655,1 605,206 655,412 455,412 505,206" fill="var(--mist-light)" opacity="0.55"/>
    <g stroke="var(--paper)" stroke-width="5" fill="none">
      <line x1="337" y1="1" x2="405" y2="206"/>
      <line x1="405" y1="206" x2="337" y2="412"/>
      <line x1="773" y1="1" x2="705" y2="206"/>
      <line x1="705" y1="206" x2="773" y2="412"/>
    </g>
    <g stroke="var(--mist)" stroke-width="1" fill="none">
      <line x1="460" y1="1" x2="395" y2="206"/>
      <line x1="395" y1="206" x2="460" y2="412"/>
      <line x1="650" y1="1" x2="715" y2="206"/>
      <line x1="715" y1="206" x2="650" y2="412"/>
    </g>

    <text class="phone" x="555" y="48" text-anchor="middle">512.637.4185</text>

    <!-- brand name -->
    <circle cx="555" cy="150" r="9" fill="var(--red)"/>
    <text class="brand-name" text-anchor="middle">
      <tspan x="555" y="200">COPPER</tspan>
      <tspan x="555" y="238">LANTERN</tspan>
      <tspan x="555" y="276">SWEETS</tspan>
    </text>

    <!-- left claims -->
    <use href="#star" class="star" x="226" y="124"/>
    <text class="claim" text-anchor="middle">
      <tspan x="226" y="162">VEGAN</tspan>
      <tspan x="226" y="190">GLUTEN FREE</tspan>
      <tspan x="226" y="218" textLength="280" lengthAdjust="spacingAndGlyphs">FAIR TRADE CHOCOLATE</tspan>
      <tspan x="226" y="246">ALLERGY FRIENDLY</tspan>
      <tspan x="226" y="274">ORGANIC</tspan>
    </text>
    <use href="#star" class="star" x="226" y="292"/>

    <!-- right claims -->
    <use href="#star" class="star" x="885" y="117"/>
    <text class="claim" text-anchor="middle">
      <tspan x="885" y="158">HAND MADE</tspan>
    </text>
    <rect role="img" aria-label="Small scroll flourish" x="862" y="174" width="46" height="16" rx="8" fill="var(--teal)" opacity="0.8"/>
    <text class="claim" text-anchor="middle">
      <tspan x="885" y="224">LOCALLY</tspan>
      <tspan x="885" y="252" textLength="194" lengthAdjust="spacingAndGlyphs">MADE IN AUSTIN</tspan>
      <tspan x="885" y="280">TEXAS</tspan>
    </text>
    <use href="#star" class="star" x="885" y="298"/>

    <!-- web and social -->
    <rect role="img" aria-label="Ornamental curly bracket" x="270" y="336" width="11" height="64" rx="5" fill="var(--red)"/>
    <rect role="img" aria-label="Ornamental curly bracket" x="829" y="336" width="11" height="64" rx="5" fill="var(--red)"/>
    <text class="web" x="555" y="366" text-anchor="middle" textLength="458" lengthAdjust="spacingAndGlyphs">WWW.COPPERLANTERNSWEETSATX.COM</text>
    <text class="social" x="555" y="391" text-anchor="middle" textLength="520" lengthAdjust="spacingAndGlyphs">CHECK US OUT ON INSTAGRAM : <tspan class="social-handle">COPPERLANTERNSWEETS</tspan></text>
  </svg>
</div>
</body>
</html>
```